Website Design for Harbor Guidepost

I am looking to create a website to help military members who are currently serving or have served to have a mentor. The military does an awful job and providing or offering a mentor program. People need someone they can come to with career advice with promotions, networking, building resumes, and pinging ideas off of on the occasion. I want a place where active and separated military members can come to, sign up and pick a program of offerings that make sense. They would register annually, pay for a membership package (can choose up to three) and then get support they need. Annual registration fees would be as follows and they would need to send payment through Paypal or other electronic means (credit card, eft, paypal, echeck, whatever).

I envision some type of registration that centers around the packages offered - this will be where the revision comes in once the framework is completed.

I am looking for very creative designs, and content, given the above, with verbiage around mentorship program. Please be creative for the design, and also put together three packages and price points for them three packages - put together what it would include in each package. We can modify as necessary during revisions. Final design should communicate military members in uniform with corporate leaders, something warm and inviting are important. I also want the abiity to really get this adversited and in the market for people to stumble across it easily.

I have purchased the domain already - harborguidepost.com

Target Market(s)

Military, Veterans

Number of Pages Required

1 page

Requirements
Must have
• Military member with corporate look
• Modern and wide
• Warm and inviting
• Registration with ability to collect through PayPal, eCheck, Credit Card, etc)
• Creative design and content for the website based on what is described in the description
• About Section which has information about leadership team
• Contact Us
• Register
• 3 creative packages of what would be included (design this and the content keeping in mind the description)
• Content and the framework
• Some type of packages to consider (just examples but also needs mentoring options:
• https://www.careerquillstudio.com/
• https://www.jobcrestpro.com/
• We are not going to ba resume writing service but we will offer it as part of our solution - I really want it to be focused around mentorship for job development, professional advice, interacting with peers, managers, leaders (using military acronyms like Supervisors and Leaders NCO's, Officers, etc)
• Blog so we can post topics and interact and respond to questions people have etc

```html
<!DOCTYPE html>
<html lang="en">
<head>
<meta charset="utf-8">
<title>Harbor Guidepost</title>
<link rel="stylesheet" href="https://fonts.googleapis.com/css2?family=Poppins:wght@400;500;600;700&family=Open+Sans:wght@400;600&display=swap">
<style>
:root{
  --blue:#1a8fd1;
  --orange:#f7a70b;
  --ink:#1b1b1b;
  --muted:#6d6d6d;
  --camo-dark:#252a1e;
  --camo-mid:#3c4430;
  --white:#ffffff;
  --footer:#e6e6e4;
}
*{box-sizing:border-box;margin:0;padding:0}
html,body{width:1200px;height:2980px;overflow:hidden}
body{position:relative;font-family:"Open Sans",sans-serif;color:var(--ink);background:var(--white)}
.abs{position:absolute}
h1,h2,h3,h4,.nav,.btn{font-family:"Poppins",sans-serif}

/* header */
.brand{left:86px;top:40px;display:flex;align-items:center;gap:10px;font-family:"Poppins",sans-serif;font-weight:700;font-size:25px;color:var(--blue);letter-spacing:.3px}
.brand-mark{width:26px;height:26px;background:var(--blue)}
.signup{top:24px;height:30px;font-size:12px;font-weight:500;color:var(--white);display:flex;align-items:center;justify-content:center;font-family:"Poppins",sans-serif}
.signup.active{left:672px;width:186px;background:var(--orange)}
.signup.separated{left:870px;width:244px;background:var(--blue)}
.nav{right:86px;top:70px;display:flex;gap:34px;font-size:14px;font-weight:500}

/* hero */
.hero{left:0;top:112px;width:1200px;height:486px;background:linear-gradient(180deg,#4a4f55 0%,#2c3138 55%,#1d2228 100%)}
.hero-title{left:0;width:1200px;text-align:center;color:var(--white)}
.hero-sub{top:262px;font-family:"Poppins",sans-serif;font-size:32px;font-weight:500}
.hero-main{top:304px;font-family:"Poppins",sans-serif;font-size:54px;font-weight:600}
.btn-register{left:506px;top:390px;width:190px;height:46px;background:var(--orange);color:var(--white);font-size:17px;font-weight:500;display:flex;align-items:center;justify-content:center}
.arrow{top:338px;width:40px;height:40px;border-radius:50%;background:var(--white);display:flex;align-items:center;justify-content:center}

/* card grids */
.intro-card{width:246px;height:314px;background:linear-gradient(160deg,#4a5138,#262b1f 60%,#34402a);color:var(--white);text-align:center;padding:0 16px;display:flex;flex-direction:column;justify-content:center;align-items:center}
.intro-card h2{font-size:26px;font-weight:600;margin-bottom:10px}
.intro-card p{font-size:12px;line-height:21px}
.outline-btn{margin-top:18px;border:1px solid var(--white);padding:4px 16px;font-size:13px;font-family:"Poppins",sans-serif}
.card{width:246px}
.card .photo{width:246px;height:154px}
.card h3{font-size:17px;font-weight:500;margin:26px 12px 0}
.card .tag{font-size:11px;margin:4px 12px 0;font-family:"Poppins",sans-serif}
.card p{font-size:11.5px;line-height:22px;color:var(--muted);margin:8px 12px 0}
.card .more{font-size:12px;margin:10px 12px 0;font-family:"Poppins",sans-serif;display:block}

/* about */
.about-photo{left:0;top:1062px;width:604px;height:396px;background:linear-gradient(120deg,#6b6f73,#2c2f33 55%,#8a8d86)}
.about-panel{left:604px;top:1062px;width:596px;height:396px;background:linear-gradient(150deg,#1c2016,#363d2b 55%,#22271b);color:var(--white);padding:70px 40px 0 38px}
.about-panel h2{font-size:33px;font-weight:400;margin-bottom:14px}
.about-panel p{font-size:15.5px;line-height:27px;color:#e6e6e6}
.btn-team{display:inline-flex;margin-top:20px;background:var(--blue);border:1px solid #9fd3f2;color:var(--white);height:44px;padding:0 28px;align-items:center;font-size:16px;font-family:"Poppins",sans-serif}

/* blog */
.section-title{left:0;width:1200px;text-align:center;font-size:33px;font-weight:600}
.post-photo{width:176px;height:170px}
.date{width:48px;height:54px;background:var(--orange);color:var(--white);text-align:center;font-family:"Poppins",sans-serif}
.date b{display:block;font-size:30px;line-height:36px;font-weight:600}
.date span{font-size:8px}
.post{width:284px}
.post h4{font-size:17px;font-weight:500;color:var(--blue);line-height:26px}
.post p{font-size:12px;line-height:20px;color:var(--muted);margin-top:6px}
.post .more{font-size:12px;color:var(--blue);margin-top:10px;display:block;font-family:"Poppins",sans-serif}

/* newsletter */
.newsletter{left:0;top:2282px;width:1200px;height:330px;background:linear-gradient(135deg,#2a2f22,#4b5539 35%,#2e3425 60%,#56604a 100%)}
.news-title{left:0;top:2346px;width:1200px;text-align:center;color:var(--white);font-family:"Poppins",sans-serif;font-size:33px;letter-spacing:5px}
.news-sub{left:0;top:2396px;width:1200px;text-align:center;color:var(--white);font-size:13px;line-height:21px}
.email{left:312px;top:2454px;width:414px;height:50px;background:var(--white);font-size:12px;color:#999;padding-left:26px;display:flex;align-items:center;font-style:italic}
.subscribe{left:746px;top:2454px;width:162px;height:50px;background:var(--orange);color:var(--white);font-weight:600;letter-spacing:2px;font-size:16px;display:flex;align-items:center;justify-content:center}
.social{left:498px;top:2526px;display:flex;gap:10px}
.social span{width:38px;height:38px;border-radius:50%}

/* footer */
.footer{left:0;top:2612px;width:1200px;height:368px;background:var(--footer)}
.foot-brand{left:142px;top:2754px;width:230px;text-align:center;font-family:"Poppins",sans-serif;font-weight:700;font-size:22px;color:var(--blue)}
.foot-mark{left:232px;top:2674px;width:52px;height:52px;background:var(--blue)}
.pay{top:2798px;width:58px;height:34px}
.divider-v{top:2674px;width:1px;height:190px;background:#c9c9c6}
.foot-head{font-family:"Poppins",sans-serif;font-size:17px;color:#8a8a8a}
.contact-row{left:532px;display:flex;align-items:flex-start;gap:18px;font-size:14px;color:#8a8a8a;line-height:26px}
.quick{left:1006px;top:2720px;list-style:none;font-size:11px;line-height:26px;color:#6a6a6a;text-transform:uppercase;font-family:"Poppins",sans-serif}
.quick li::before{content:"› ";}
.rule{left:86px;top:2898px;width:1028px;height:1px;background:#c9c9c6}
.copyright{left:0;top:2924px;width:1200px;text-align:center;font-size:14px;color:#555}
</style>
</head>
<body>

<!-- header -->
<div class="abs brand"><span class="brand-mark"></span>HARBOR GUIDEPOST</div>
<div class="abs signup active">Active Member Sign Up</div>
<div class="abs signup separated">Separated Military Member Sign Up</div>
<nav class="abs nav"><span>Home</span><span>About</span><span>What We Do</span><span>Packages</span><span>Blog</span><span>Contact Us</span></nav>

<!-- hero -->
<div class="abs hero" role="img" aria-label="Soldier and business leader shaking hands over a city skyline"></div>
<div class="abs hero-title hero-sub">Welcome to</div>
<div class="abs hero-title hero-main">Harbor Guidepost</div>
<div class="abs btn btn-register">Register Now &rsaquo;</div>
<div class="abs arrow" style="left:48px"><svg width="14" height="14" viewBox="0 0 14 14"><path d="M9 2 4 7l5 5" stroke="#111" stroke-width="2.5" fill="none"/></svg></div>
<div class="abs arrow" style="left:1112px"><svg width="14" height="14" viewBox="0 0 14 14"><path d="M5 2l5 5-5 5" stroke="#111" stroke-width="2.5" fill="none"/></svg></div>

<!-- what we offer -->
<div class="abs intro-card" style="left:86px;top:668px">
  <h2>What We Offer?</h2>
  <p>Lorem Ipsum is simply dummy text of the printing and typesetting industry. Lorem Ipsum has been the industry's1500s</p>
  <span class="outline-btn">Read More &rsaquo;</span>
</div>
<div class="abs card" style="left:348px;top:668px">
  <div class="photo" role="img" aria-label="Mentor and client talking at a desk" style="background:linear-gradient(135deg,#2d4a7a,#8aa2c4)"></div>
  <h3>Career Advice</h3>
  <p>Lorem Ipsum is simply dummy text of the printing and typesetting industry. Lorem Ipsum industry's1500s</p>
  <span class="more">Read More &gt;</span>
</div>
<div class="abs card" style="left:610px;top:668px">
  <div class="photo" role="img" aria-label="Networking concept with connected contacts" style="background:linear-gradient(135deg,#6b3f4e,#c49aa0)"></div>
  <h3>Networking</h3>
  <p>Lorem Ipsum is simply dummy text of the printing and typesetting industry. Lorem Ipsum industry's1500s</p>
  <span class="more">Read More &gt;</span>
</div>
<div class="abs card" style="left:872px;top:668px">
  <div class="photo" role="img" aria-label="Hands holding a printed resume" style="background:linear-gradient(135deg,#9a9a98,#3c3c3e)"></div>
  <h3>Building Resumes</h3>
  <p>Lorem Ipsum is simply dummy text of the printing and typesetting industry. Lorem Ipsum industry's1500s</p>
  <span class="more">Read More &gt;</span>
</div>

<!-- about -->
<div class="abs about-photo" role="img" aria-label="Service member in uniform typing on a laptop"></div>
<div class="abs about-panel">
  <h2>ABOUT US</h2>
  <p>Sed ut perspiciatis unde omnis iste natus error sit voluptatem accusantium doloremque laudantium, totam rem aperiam, eaque ipsa quae ab illo inventore veritatis et quasi architecto beatae vitae dicta sunt explicabo. Nemo enim ipsam voluptatem quia voluptas sit aspernatur aut odit aut fugit, sed quia</p>
  <span class="btn-team">Meet The Team</span>
</div>

<!-- packages -->
<div class="abs intro-card" style="left:86px;top:1538px;height:330px">
  <h2>Our Packages</h2>
  <p>Lorem Ipsum is simply dummy text of the printing and typesetting industry. Lorem Ipsum has been the industry's1500s</p>
</div>
<div class="abs card" style="left:348px;top:1538px">
  <div class="photo" role="img" aria-label="Graduate in cap holding a diploma" style="background:linear-gradient(135deg,#e9e6e2,#b9a99a)"></div>
  <h3>Student – $110</h3>
  <div class="tag">College, Graduate School Admission</div>
  <p>Lorem Ipsum is simply dummy text of the printing and typesetting industry. Lorem Ipsum industry's1500s</p>
  <span class="more">Learn More &gt;</span>
</div>
<div class="abs card" style="left:610px;top:1538px">
  <div class="photo" role="img" aria-label="Soldiers on patrol in the field" style="background:linear-gradient(135deg,#4b5a32,#7d7a55)"></div>
  <h3>Military – $230</h3>
  <div class="tag">2+ years</div>
  <p>Lorem Ipsum is simply dummy text of the printing and typesetting industry. Lorem Ipsum industry's1500s</p>
  <span class="more">Learn More &gt;</span>
</div>
<div class="abs card" style="left:872px;top:1538px">
  <div class="photo" role="img" aria-label="Columned federal government building" style="background:linear-gradient(180deg,#cfcfcd,#8e8e8c)"></div>
  <h3>Federal – $230</h3>
  <div class="tag">Federal government jobs</div>
  <p>Lorem Ipsum is simply dummy text of the printing and typesetting industry. Lorem Ipsum industry's1500s</p>
  <span class="more">Learn More &gt;</span>
</div>

<!-- blog -->
<h2 class="abs section-title" style="top:1946px">LATEST BLOG</h2>
<div class="abs post-photo" role="img" aria-label="Colleagues reviewing work at a computer" style="left:96px;top:2026px;background:linear-gradient(135deg,#b8c3cc,#5d7385)"></div>
<div class="abs date" style="left:226px;top:2026px"><b>15</b><span>Feb 2018</span></div>
<div class="abs post" style="left:296px;top:2026px">
  <h4>The standard Lorem Ipsum passage, used since the 1500s</h4>
  <p>Lorem ipsum dolor sit amet, consectetur adipiscing elit, sed do eiusmod tempor incididunt ut labore et dolore magna aliqua.</p>
  <span class="more">Read More &rsaquo;</span>
</div>
<div class="abs post-photo" role="img" aria-label="Professional woman working at a desk" style="left:614px;top:2026px;background:linear-gradient(135deg,#e8e2d8,#b49a7e)"></div>
<div class="abs date" style="left:744px;top:2026px"><b>14</b><span>Feb 2018</span></div>
<div class="abs post" style="left:816px;top:2026px">
  <h4>The standard Lorem Ipsum passage, used since the 1500s</h4>
  <p>Lorem ipsum dolor sit amet, consectetur adipiscing elit, sed do eiusmod tempor incididunt ut labore et dolore magna aliqua.</p>
  <span class="more">Read More &rsaquo;</span>
</div>

<!-- newsletter -->
<div class="abs newsletter" role="img" aria-label="Camouflage background"></div>
<div class="abs news-title">NEWSLETTER SIGN UP</div>
<div class="abs news-sub">Lorem ipsum dolor sit amet, consectetur adipisicing elit,sed do<br>eiusmod ut labore et dolore</div>
<div class="abs email">Enter your email...</div>
<div class="abs btn subscribe">SUBSCRIBE</div>
<div class="abs social">
  <span style="background:#3b5a9a"></span><span style="background:#2aa3ef"></span><span style="background:#d8473a"></span><span style="background:#e02a20"></span><span style="background:#c8338a"></span>
</div>

<!-- footer -->
<div class="abs footer"></div>
<div class="abs foot-mark"></div>
<div class="abs foot-brand">HARBOR GUIDEPOST</div>
<div class="abs pay" style="left:158px;background:#f2f2f2;border:1px solid #ccc"></div>
<div class="abs pay" style="left:230px;background:#c9b27a"></div>
<div class="abs pay" style="left:298px;background:#1d4c9a"></div>
<div class="abs divider-v" style="left:460px"></div>
<div class="abs divider-v" style="left:942px"></div>
<div class="abs foot-head" style="left:532px;top:2670px">Contact Info:</div>
<div class="abs contact-row" style="top:2710px">
  <svg width="12" height="16" viewBox="0 0 12 16" style="margin-top:5px"><path d="M6 0a6 6 0 0 0-6 6c0 4.5 6 10 6 10s6-5.5 6-10a6 6 0 0 0-6-6zm0 8.5A2.5 2.5 0 1 1 6 3.5a2.5 2.5 0 0 1 0 5z" fill="#8a8a8a"/></svg>
  <div>Harbor Guidepost<br>418 Anchor Lane, Bayport, United States</div>
</div>
<div class="abs contact-row" style="top:2784px">
  <svg width="14" height="14" viewBox="0 0 14 14" style="margin-top:6px"><path d="M3 0l2.5 3.5-1.5 1.8a8 8 0 0 0 4.7 4.7L10.5 8.5 14 11l-1.5 3C6 14 0 8 0 1.5z" fill="#8a8a8a"/></svg>
  <div>0198 765 432</div>
</div>
<div class="abs contact-row" style="top:2826px">
  <svg width="14" height="11" viewBox="0 0 14 11" style="margin-top:8px"><rect width="14" height="11" fill="#8a8a8a"/><path d="M0 0l7 6 7-6" stroke="#e6e6e4" fill="none"/></svg>
  <div>info@harborguidepost.com</div>
</div>
<div class="abs foot-head" style="left:1006px;top:2670px">Quick Links:</div>
<ul class="abs quick"><li>Home</li><li>About</li><li>What We Do</li><li>Packages</li><li>Blog</li><li>Contact Us</li></ul>
<div class="abs rule"></div>
<div class="abs copyright">Copyright © 2018. Harbor Guidepost. All rights reserved.</div>

</body>
</html>
```